Web page design for a startup, no coding

Quarrynest is a Data mining startup helping companies get data from websites. We’re looking to revamp our website to make it more professional and conversation friendly.
I need a designer to design the website in PSD and Once the PSD is done, the HTML design will be awarded as a separate job. We’ll need continues improvements to the design based on the user behaviour in the site and this can be a long term work for the right designer.
Target Market(s)
Big data, Data Mining
Industry/Entity Type
Business Software
Number of Pages Required
5+ page
Requirements
Must have
- Refer to the doc
Nice to have
- Refer to the doc
Should not have
- Refer to the doc

```html
<!DOCTYPE html>
<html lang="en">
<head>
<meta charset="utf-8">
<title>Quarrynest — Turn Websites Into Structured Data feeds</title>
<link href="https://fonts.googleapis.com/css2?family=Nunito+Sans:wght@300;400;600;700&display=swap" rel="stylesheet">
<style>
:root{
  --amber:#fdb515;
  --slate:#777879;
  --ink:#1f1f1f;
  --muted:#8a8a8a;
  --band:#f2f2f2;
  --white:#ffffff;
  --line:#d9d9d9;
}
*{box-sizing:border-box;margin:0;padding:0}
html,body{width:1200px;height:2459px;overflow:hidden}
body{position:relative;font-family:"Nunito Sans",Arial,sans-serif;color:var(--ink);background:var(--white)}
.abs{position:absolute}

/* hero */
.hero{left:0;top:0;width:1200px;height:585px;overflow:hidden}
.hero-photo{position:absolute;inset:0;background:
  radial-gradient(ellipse at 62% 40%, #cfd3d6 0%, #9ea4a8 35%, #6d7377 70%, #4b5053 100%);}
.hero-shade{position:absolute;inset:0;background:rgba(40,40,40,.35)}
.brand{left:159px;top:26px;display:flex;align-items:center;gap:12px;color:var(--white);font-size:34px;font-weight:400;letter-spacing:.2px}
.brand-mark{width:22px;height:22px;border:2px solid currentColor;border-radius:3px}
.nav{top:44px;left:598px;display:flex;gap:28px;color:var(--white);font-size:18px;font-weight:600}
.hero-title{top:220px;left:0;width:1200px;text-align:center;color:var(--white);font-size:37px;font-weight:600}
.hero-sub{top:276px;left:170px;width:860px;text-align:center;color:var(--white);font-size:19px;line-height:27px}
.btn{display:flex;align-items:center;justify-content:center;background:var(--amber);color:var(--white);font-weight:600}
.hero-btn{left:518px;top:352px;width:170px;height:43px;font-size:18px}
.dots{left:561px;top:557px;display:flex;gap:9px}
.dots span{width:13px;height:13px;border-radius:50%;background:var(--white)}
.dots span:first-child{background:transparent;border:2px solid var(--white)}

/* clients */
.clients{left:0;top:585px;width:1200px;height:112px;display:flex;align-items:center;justify-content:center;gap:52px;color:#6f6f6f;font-size:27px;font-weight:600}

/* uses */
.uses{left:0;top:697px;width:1200px;height:524px;background:var(--band)}
.uses-title{position:absolute;top:58px;left:0;width:1200px;text-align:center;font-size:26px;line-height:33px;font-weight:400}
.use{position:absolute;width:340px}
.use h3{font-size:17px;font-weight:400;margin-bottom:5px}
.use p{font-size:11.5px;line-height:16px;color:var(--muted)}
.use.left{left:124px;text-align:right}
.use.right{left:726px}
.use-icon{position:absolute;width:70px;height:70px;border-radius:50%;background:var(--white);border:1.5px solid var(--line);display:flex;align-items:center;justify-content:center}

/* why */
.why-title{top:1280px;left:0;width:1200px;text-align:center;font-size:30px;font-weight:400}
.hexes{left:152px;top:1323px;width:896px;height:254px}
.hex-label{position:absolute;width:223px;text-align:center;color:var(--white)}
.hex-label h3{font-size:15.5px;font-weight:700;margin-bottom:8px}
.hex-label p{font-size:11px;line-height:16px;padding:0 34px;opacity:.95}

/* contact */
.contact{left:0;top:1639px;width:1200px;height:480px;overflow:hidden}
.contact-photo{position:absolute;inset:0;background:linear-gradient(120deg,#e4e6e8 0%,#f3f4f5 45%,#eceef0 75%,#dfe2e4 100%)}
.contact-title{position:absolute;top:50px;left:0;width:1200px;text-align:center;font-size:30px;font-weight:400}
.contact-sub{position:absolute;top:100px;left:0;width:1200px;text-align:center;font-size:18px;line-height:28px;color:#555}
.field{position:absolute;background:var(--white);border:1px solid #cfcfcf;font-size:14px;color:#777;padding:0 18px;display:flex;align-items:center}
.field.area{align-items:flex-start;padding-top:12px}
.submit{left:534px;top:393px;width:135px;height:36px;font-size:15px;position:absolute}

/* footer */
.footer{left:0;top:2119px;width:1200px;height:340px}
.fcol{position:absolute;top:46px}
.fcol h4{color:var(--amber);font-size:21px;font-weight:400;margin-bottom:10px}
.fcol li{list-style:none;font-size:14px;color:#555;line-height:28px}
.socials{display:flex;gap:11px}
.socials span{width:34px;height:34px;border-radius:50%;background:var(--amber)}
.foot-brand{left:846px;top:66px;display:flex;align-items:center;gap:12px;color:#555;font-size:34px}
.divider{left:157px;top:274px;width:885px;height:1px;background:var(--line)}
.copy{left:0;top:292px;width:1200px;text-align:center;font-size:12px;color:#a0a0a0}
</style>
</head>
<body>

<header class="abs hero">
  <div class="hero-photo" role="img" aria-label="Photo of a person at a desk looking at a monitor showing business charts, with a potted plant"></div>
  <div class="hero-shade"></div>
  <div class="abs brand"><span class="brand-mark"></span>Quarrynest</div>
  <nav class="abs nav"><span>Solutions</span><span>Pricing</span><span>Company</span><span>Get free Quote</span></nav>
  <h1 class="abs hero-title">Turn Websites Into Structured Data feeds</h1>
  <p class="abs hero-sub">Easily get structured data feeds from any website through our cloud based data as a service platform. No programming ,Servers or Expensive Softwares required</p>
  <div class="abs btn hero-btn">Get free Quote</div>
  <div class="abs dots"><span></span><span></span><span></span><span></span></div>
</header>

<section class="abs clients">
  <span>Brellow</span><span>Taskmere</span><span>VANTORA</span><span>Zinnly</span><span>launchpile</span><span>holbrenn</span>
</section>

<section class="abs uses">
  <h2 class="uses-title">Businesses of all sizes use our clean data feeds to Quickly build apps,<br>Experiment with fresh ideas and Solve business problems</h2>

  <div class="use left" style="top:192px"><h3>ECommerce</h3><p>Our Ecommerce product data feeds gives you access<br>to structured product information like pricing,,</p></div>
  <div class="use left" style="top:288px"><h3>Lead Generation</h3><p>We help find quality leads for your business by<br>extracting public data from all kind of sources like</p></div>
  <div class="use left" style="top:390px"><h3>SERP Tracking</h3><p>Our SERP data feeds gives companies access to<br>Search Engine rankings of any keywords from search</p></div>
  <div class="use right" style="top:192px"><h3>News Aggregation</h3><p>We help businesses build their own unique news<br>data feeds by aggregating data from news sites</p></div>
  <div class="use right" style="top:288px"><h3>Recruiting</h3><p>We help recruiters automate scouting candidate<br>profiles from different online sources</p></div>
  <div class="use right" style="top:390px"><h3>Build your App</h3><p>We help businesses quickly build their apps on top<br>of our scalable data extraction infrastructure</p></div>

  <div class="use-icon" style="left:480px;top:191px"><svg width="36" height="32" viewBox="0 0 36 32" fill="none" stroke="#fdb515" stroke-width="2"><rect x="2" y="2" width="32" height="26"/><line x1="2" y1="8" x2="34" y2="8"/><path d="M10 13h3l3 8h9l2-6H15"/><circle cx="17" cy="24" r="1.5"/><circle cx="24" cy="24" r="1.5"/></svg></div>
  <div class="use-icon" style="left:480px;top:287px"><svg width="34" height="34" viewBox="0 0 34 34" fill="#fdb515"><circle cx="17" cy="10" r="6"/><path d="M6 32c0-8 5-13 11-13s11 5 11 13z"/><circle cx="6" cy="13" r="4"/><circle cx="28" cy="13" r="4"/></svg></div>
  <div class="use-icon" style="left:480px;top:389px"><svg width="40" height="26" viewBox="0 0 40 26" fill="none" stroke="#fdb515" stroke-width="2"><path d="M2 18l8-8 6 6 4-4"/><circle cx="25" cy="10" r="6"/><line x1="29" y1="14" x2="35" y2="20"/><path d="M32 8l6-4"/></svg></div>
  <div class="use-icon" style="left:637px;top:191px"><svg width="32" height="32" viewBox="0 0 32 32" fill="none" stroke="#fdb515" stroke-width="2"><rect x="6" y="3" width="22" height="26"/><path d="M6 9H3v18a2 2 0 0 0 3 2"/><line x1="11" y1="9" x2="23" y2="9"/><line x1="11" y1="14" x2="23" y2="14"/><line x1="11" y1="19" x2="23" y2="19"/><line x1="11" y1="24" x2="19" y2="24"/></svg></div>
  <div class="use-icon" style="left:637px;top:287px"><svg width="36" height="36" viewBox="0 0 36 36" fill="none" stroke="#fdb515" stroke-width="2.2"><circle cx="18" cy="18" r="12"/><circle cx="18" cy="18" r="4" fill="#fdb515"/><line x1="18" y1="1" x2="18" y2="9"/><line x1="18" y1="27" x2="18" y2="35"/><line x1="1" y1="18" x2="9" y2="18"/><line x1="27" y1="18" x2="35" y2="18"/></svg></div>
  <div class="use-icon" style="left:637px;top:389px"><svg width="22" height="36" viewBox="0 0 22 36" fill="none" stroke="#fdb515" stroke-width="2"><rect x="2" y="2" width="18" height="32" rx="3"/><line x1="2" y1="7" x2="20" y2="7"/><line x1="2" y1="28" x2="20" y2="28"/></svg></div>
</section>

<h2 class="abs why-title">Why Us</h2>
<div class="abs hexes">
  <svg width="896" height="254" viewBox="0 0 896 254">
    <polygon points="111.5,0 223,63.5 223,190.5 111.5,254 0,190.5 0,63.5" fill="#fdb515"/>
    <polygon points="335.5,0 447,63.5 447,190.5 335.5,254 224,190.5 224,63.5" fill="#777879"/>
    <polygon points="559.5,0 671,63.5 671,190.5 559.5,254 448,190.5 448,63.5" fill="#fdb515"/>
    <polygon points="783.5,0 895,63.5 895,190.5 783.5,254 672,190.5 672,63.5" fill="#777879"/>
    <g fill="none" stroke="#fff" stroke-width="2.4">
      <path d="M88 50h14a6 6 0 1 1 12 0h14v16a6 6 0 1 1 0 12v16h-40z"/>
      <line x1="108" y1="62" x2="108" y2="94"/>
      <ellipse cx="335.5" cy="48" rx="22" ry="7"/>
      <path d="M313.5 48v34c0 4 10 7 22 7s22-3 22-7V48"/>
      <path d="M313.5 60c0 4 10 7 22 7s22-3 22-7M313.5 72c0 4 10 7 22 7s22-3 22-7"/>
      <path d="M534 94h50M536 86l14-14 9 9 18-18"/><path d="M569 62h9v9"/>
      <path d="M762 76h10l8 6h14a4 4 0 0 1 0 8h-16M762 94h12l22-6 14-10"/>
    </g>
    <g fill="#fff" font-family="Nunito Sans,Arial,sans-serif" font-size="9" font-weight="700">
      <text x="770" y="46">1010</text><text x="782" y="58">010</text><text x="770" y="70">1001</text>
    </g>
  </svg>
  <div class="hex-label" style="left:0;top:120px"><h3>Solve Real Problems</h3><p>Quarrynest provides a fully managed Big Data As A Service. You can easily plug our data feeds into your favourite</p></div>
  <div class="hex-label" style="left:224px;top:120px"><h3>Clean Data</h3><p>We follow a strict quality assurance process and a Machine learning based Q&amp;A system to ensure the</p></div>
  <div class="hex-label" style="left:448px;top:120px"><h3>Customer Success</h3><p>Ensuring Customer success is our first priority. Our customer success team consists of experienced</p></div>
  <div class="hex-label" style="left:672px;top:120px"><h3>Data Wrangling Support</h3><p>Quarrynest helps those who need data wrangling support by providing profiling, filtering</p></div>
</div>

<section class="abs contact">
  <div class="contact-photo" role="img" aria-label="Photo of a white desk with a keyboard, notebook, coffee cup and mouse"></div>
  <h2 class="contact-title">We’re here to help!</h2>
  <p class="contact-sub">We're friendly and available to help solve your data extraction problems.<br>Fill the form below to contact us. Let us do the heavy lifting for youa</p>
  <div class="field" style="left:292px;top:192px;width:377px;height:38px">Email address</div>
  <div class="field" style="left:677px;top:192px;width:231px;height:38px">Your Monthly Budget</div>
  <div class="field area" style="left:292px;top:241px;width:616px;height:133px">Your Message</div>
  <div class="btn submit">SUBMIT</div>
</section>

<footer class="abs footer">
  <div class="fcol" style="left:157px"><h4>Quick Links</h4><ul><li>Blog</li><li>Answers</li><li>Case Studies</li><li>Slide</li></ul></div>
  <div class="fcol" style="left:379px"><h4>Resources</h4><ul><li>Startup Partner program</li><li>FAQ</li><li>Careers</li></ul></div>
  <div class="fcol" style="left:616px"><h4>Follow Us</h4><div class="socials"><span></span><span></span><span></span><span></span></div></div>
  <div class="abs foot-brand"><span class="brand-mark" style="border-color:#555"></span>Quarrynest</div>
  <div class="abs divider"></div>
  <p class="abs copy">© 2016 Company Name &nbsp;All right reserved &nbsp;Term of Use</p>
</footer>

</body>
</html>
```